Give my personal webpage more appeal!

I need my CV website improved - drmeganholt.com.au.
I am using the template KESTREL from pagecraftly. i would like to keep the already existing theme but am open to suggestions.
Please focus on imagery, colour scheme, and textures to enhance the appeal and look of the page.
The content is there, but now I need a designer to improve the look of my page.
I need styling, royalty-free unique modern images to make the page professional, personal and friendly.
I work in healthcare, so I'm a people person.
I teach professionals and I treat a lot of families.

Target Market(s)

Parents, Professional Healthcare providers

Number of Pages Required

1 page

Font styles to use
Serif
Sans Serif

Requirements
Must have
• My face - image at the top, all the information already contained in it.
• Links to the websites I manage such as my blog.
• One Page website.
• All the information it already contains with the ability to have more.
• Ideally, we would keep the same format for the page although I'm happy to expand column and change the page's structure with in the theme template KESTREL.
Nice to have
• The current KESTREL template. I would like to keep the already existing theme but am open to suggestions.
Should not have
• Multiple pages.

```html
<!DOCTYPE html>
<html lang="en">
<head>
<meta charset="utf-8">
<title>Dr Megan Holt</title>
<link href="https://fonts.googleapis.com/css2?family=Lato:wght@300;400;700;900&family=Open+Sans:wght@400;600&family=Dancing+Script:wght@500&display=swap" rel="stylesheet">
<style>
:root{
  --sidebar:#242424;
  --dark:#262626;
  --row:#383838;
  --row-line:#4a4a4a;
  --yellow:#e9a91c;
  --magenta:#8a1d4b;
  --white:#ffffff;
  --text:#555555;
  --muted:#9a9a9a;
  --orange:#f0a21e;
  --pink:#e0195a;
  --blue:#2a7fd0;
  --red:#e8173c;
  --green:#3bb54a;
  --purple:#6b2c8f;
}
*{box-sizing:border-box;margin:0;padding:0}
html,body{width:1200px;height:4369px;overflow:hidden}
body{position:relative;background:var(--white);font-family:"Open Sans",Arial,sans-serif;color:var(--text)}
.sidebar{position:absolute;left:0;top:0;width:198px;height:4369px;background:var(--sidebar)}
.brand{position:absolute;left:22px;top:32px;font-family:"Lato",sans-serif;font-weight:400;font-size:22px;color:var(--white);letter-spacing:.5px}
.brand-sub{position:absolute;left:22px;top:62px;width:150px;height:2px;background:#555}
.nav{position:absolute;left:14px;top:118px;width:170px;list-style:none}
.nav li{height:44px;line-height:44px;border-bottom:1px solid #3a3a3a;font-family:"Lato",sans-serif;font-size:10px;font-weight:700;color:#d8d8d8;letter-spacing:.4px}
.nav li.active{color:var(--yellow)}
.main{position:absolute;left:198px;top:0;width:1002px;height:4369px}
section{position:absolute;left:0;width:1002px}
.section-title{position:absolute;left:0;width:100%;text-align:center;font-family:"Lato",sans-serif;font-weight:700;font-size:19px;letter-spacing:1px}

/* hero */
.hero{top:0;height:518px}
.hero-photo{position:absolute;inset:0;background:linear-gradient(90deg,#7d2a2e 0%,#b5434a 22%,#c05a50 34%,#6f8a46 50%,#8daa5a 72%,#a9c47b 100%)}
.hero-text{position:absolute;left:458px;top:196px;color:var(--white);font-family:"Lato",sans-serif}
.hero-welcome{font-weight:300;font-size:29px;letter-spacing:1px}
.hero-name{font-weight:400;font-size:37px;letter-spacing:1px;margin-top:4px}
.hero-degree{font-size:12px;letter-spacing:1px;margin-top:2px}

/* about */
.about{top:518px;height:158px;background:var(--yellow)}
.about-avatar{position:absolute;left:71px;top:18px;width:94px;height:94px;border-radius:50%;background:linear-gradient(#f3d8c4,#e3b390);border:4px solid var(--white)}
.about-title{position:absolute;left:195px;top:18px;font-family:"Lato",sans-serif;font-weight:700;font-size:22px;color:var(--white)}
.about-text{position:absolute;left:195px;top:54px;width:760px;font-size:10px;line-height:16px;color:var(--white)}
.about-text p+p{margin-top:6px}

/* skills */
.skills{top:676px;height:1153px}
.skills .section-title{top:38px;color:#333}
.skill-grid{position:absolute;left:64px;top:96px;width:880px;display:grid;grid-template-columns:440px 440px;grid-auto-rows:166px}
.skill-text{padding:16px 24px 0 0}
.skill-text.right{padding:16px 0 0 24px}
.skill-text h3{font-family:"Lato",sans-serif;font-size:10.5px;font-weight:700;line-height:14px;margin-bottom:6px}
.skill-text p{font-size:10px;line-height:15px;color:#666}
.skill-text p+p{margin-top:6px}
.skill-photo{position:relative}
.skill-label{position:absolute;width:140px;height:54px;padding:10px 14px;font-family:"Lato",sans-serif;font-weight:700;font-size:13px;line-height:16px;color:var(--white);text-transform:uppercase}
.label-left{left:42px;top:50px}
.label-right{right:0;top:86px}
.c-orange{color:var(--orange)} .bg-orange{background:var(--orange)}
.c-pink{color:var(--pink)} .bg-pink{background:var(--pink)}
.c-blue{color:var(--blue)} .bg-blue{background:var(--blue)}
.c-red{color:var(--red)} .bg-red{background:var(--red)}
.c-green{color:var(--green)} .bg-green{background:var(--green)}
.c-purple{color:var(--purple)} .bg-purple{background:var(--purple)}

/* experience */
.experience{top:1829px;height:636px;background:var(--dark)}
.experience .section-title{top:60px;color:var(--yellow)}
.exp-list{position:absolute;left:64px;top:116px;width:880px;list-style:none}
.exp-list li{display:flex;align-items:center;height:50px;margin-bottom:2px;background:var(--row);font-size:10px;color:#e0e0e0}
.exp-year{width:70px;height:100%;line-height:50px;text-align:center;font-family:"Lato",sans-serif;font-weight:700;font-size:13px;color:var(--white);border-right:1px solid var(--row-line)}
.exp-desc{flex:1;padding-left:18px}
.exp-plus{width:40px;text-align:center;font-size:20px;color:var(--muted);font-weight:300}

/* education */
.education{top:2465px;height:585px;background:var(--magenta);color:var(--white)}
.education .section-title{top:60px}
.edu-intro{position:absolute;left:64px;top:112px;width:880px;text-align:center;font-size:10px;line-height:16px}
.timeline-line{position:absolute;left:500px;top:232px;width:2px;height:270px;background:rgba(255,255,255,.35)}
.edu-step{position:absolute;left:480px;width:42px;height:42px;border-radius:50%;background:#a3285c;border:2px solid rgba(255,255,255,.4);text-align:center;line-height:38px;font-family:"Lato",sans-serif;font-weight:700;font-size:14px}
.edu-item{position:absolute;width:360px;font-size:9.5px;line-height:15px}
.edu-item h4{font-family:"Lato",sans-serif;font-weight:700;font-size:10.5px;letter-spacing:.3px}
.edu-item.right{left:540px}
.edu-item.left{left:100px;text-align:right}
.edu-quote{position:absolute;left:0;top:524px;width:100%;text-align:center;font-family:"Dancing Script",cursive;font-size:22px}

/* employment */
.employment{top:3050px;height:415px}
.employment .section-title{top:118px;color:#333}
.jobs{position:absolute;left:64px;top:168px;width:880px;display:grid;grid-template-columns:repeat(4,200px);column-gap:26px}
.job h4{font-family:"Lato",sans-serif;font-weight:700;font-size:10.5px;color:#333;line-height:14px}
.job .role{font-family:"Lato",sans-serif;font-weight:700;font-size:10px;color:var(--yellow);line-height:14px}
.job .years{font-size:9.5px;color:#777;line-height:14px}
.job p{margin-top:16px;font-size:10px;line-height:15px;color:#666}

/* sites */
.sites{top:3465px;height:373px}
.sites .section-title{top:56px;color:#333}
.site-grid{position:absolute;left:64px;top:111px;display:grid;grid-template-columns:repeat(4,190px);column-gap:40px}
.site-card{height:190px;border:1px solid #e2e2e2;display:flex;align-items:center;justify-content:center;gap:8px;font-family:"Lato",sans-serif;font-weight:700;font-size:20px;box-shadow:0 1px 3px rgba(0,0,0,.12)}
.site-card.light{background:var(--white);color:#222}
.site-card.dark{background:#111;color:var(--white)}
.site-dot{width:12px;height:12px;border-radius:50%;background:var(--yellow)}

/* contact */
.contact{top:3838px;height:442px}
.contact-photo{position:absolute;inset:0;background:linear-gradient(180deg,#3b3531 0%,#2a2523 50%,#1d1a19 100%)}
.contact-title{position:absolute;top:52px;left:0;width:100%;text-align:center;font-family:"Lato",sans-serif;font-weight:700;font-size:20px;color:var(--white);letter-spacing:1px}
.contact-sub{position:absolute;top:80px;left:0;width:100%;text-align:center;font-family:"Lato",sans-serif;font-weight:700;font-size:12px;color:var(--yellow)}
.field{position:absolute;left:262px;width:466px;height:28px;background:rgba(255,255,255,.16);font-size:9.5px;color:#ddd;line-height:28px;text-align:center}
.submit{position:absolute;left:442px;top:344px;width:70px;height:28px;background:var(--yellow);color:var(--white);font-family:"Lato",sans-serif;font-weight:700;font-size:10px;line-height:28px;text-align:center}

/* footer */
.footer{top:4280px;height:89px;background:#1d1d1d}
.copyright{position:absolute;left:80px;top:38px;font-size:9px;color:#999}
.footer-brand{position:absolute;left:400px;top:30px;width:160px;text-align:center;font-family:"Lato",sans-serif;font-size:19px;color:#ddd}
.social{position:absolute;top:31px;width:26px;height:26px;border-radius:50%;background:#555}
</style>
</head>
<body>

<aside class="sidebar">
  <div class="brand">dr Megan Holt</div>
  <div class="brand-sub"></div>
  <ul class="nav">
    <li class="active">ABOUT ME</li>
    <li>SKILLS</li>
    <li>PROFESSIONAL EXPERIENCES</li>
    <li>EDUCATION</li>
    <li>EMPLOYMENT</li>
    <li>MY SITES</li>
    <li>BLOG</li>
    <li>CONTACT</li>
  </ul>
</aside>

<main class="main">

  <section class="hero">
    <div class="hero-photo" role="img" aria-label="Portrait photo of Dr Megan Holt in a red top against a soft green garden background"></div>
    <div class="hero-text">
      <div class="hero-welcome">WELCOME, TO MY PAGE.</div>
      <div class="hero-name">I AM DR MEGAN HOLT</div>
      <div class="hero-degree">BSC MCHIRO DIBAK</div>
    </div>
  </section>

  <section class="about">
    <div class="about-avatar" role="img" aria-label="Small round portrait of Dr Megan Holt"></div>
    <h2 class="about-title">ABOUT ME</h2>
    <div class="about-text">
      <p>Hello, I am a Chiropractor and a Diplomate of the International College of Neuro-Muscular Studies. I am now an avid reader of nutrition, teacher, and presenter on the AK. Teaching engagements have led me to travel, national and international destinations. Thank you for visiting my page.</p>
      <p>I am mum and wife here in Brisbane. I look forward to sharing my work with you.</p>
    </div>
  </section>

  <section class="skills">
    <h2 class="section-title">SKILLS</h2>
    <div class="skill-grid">
      <div class="skill-text">
        <h3 class="c-orange">I'M BUSINESS MINDED RUNNING A CHIROPRACTIC HEALTHCARE CLINIC IN 2001</h3>
        <p>A place to employ five Chiropractors and eight support staff. Together we treated in excess of 18,000 patient appointments annually. I sold the business in 2014.</p>
        <p>2017 will see me roll out a new business strategy for a healthcare product entering the Australian market. This business will be in distribution, logistics and education of health professionals.</p>
      </div>
      <div class="skill-photo" role="img" aria-label="Photo of a business meeting around a table" style="background:linear-gradient(135deg,#8a8e96,#c9c4bc)">
        <div class="skill-label label-left bg-orange">Business Development</div>
      </div>

      <div class="skill-photo" role="img" aria-label="Photo of a seminar class with students" style="background:linear-gradient(135deg,#5d5048,#a08c78)">
        <div class="skill-label label-right bg-pink">Teaching</div>
      </div>
      <div class="skill-text right">
        <h3 class="c-pink">I LOVE THE SYMBIOTIC RELATIONSHIP I HAVE WITH MY STUDENTS</h3>
        <p>As much as I love people eager to learn what I know, I also get a kick out of sharing what I know. The sharing of ideas and technique has taken me to the stage for community talks, healthcare industry seminars, as well as international congresses.</p>
      </div>

      <div class="skill-text">
        <h3 class="c-blue">ENROLMENT USING FUNCTIONAL NEUROLOGY AND MANUAL MUSCLE TESTING</h3>
        <p>Along with manual Chiropractic adjusting skills has held me in good stead to influence the function and well being of my patients since 2002. I see anyone with a body: from athletes at the top of their careers, sports people after their careers, active people, sedentary people, elderly people, middle aged people, and of course little people.</p>
      </div>
      <div class="skill-photo" role="img" aria-label="Photo of a chiropractic treatment on a patient's back" style="background:linear-gradient(135deg,#d9cfc6,#a4958a)">
        <div class="skill-label label-left bg-blue">Chiropractic Skills</div>
      </div>

      <div class="skill-photo" role="img" aria-label="Photo of Dr Megan Holt smiling outdoors" style="background:linear-gradient(135deg,#c9cdb4,#e9e2d2)">
        <div class="skill-label label-right bg-red">Mother &amp; Love</div>
      </div>
      <div class="skill-text right">
        <h3 class="c-red">I AM A WIFE OF A WONDERFUL MAN &amp; MOTHER OF TWO</h3>
        <p>One was a bonus, and one that I birthed. I have seen the seasons of life: the tidal flow, the ups and downs and the greatness that comes with positive thinking, gratefulness, persistence, hard work and a genuine interest and care for the people in our lives.</p>
      </div>

      <div class="skill-text">
        <h3 class="c-green">I HAVE A SPECIAL INTEREST IN PRODUCT LAUNCHING</h3>
        <p>Using the power of social media connectedness with our national network of colleagues and sensitive targeted marketing strategies.</p>
      </div>
      <div class="skill-photo" role="img" aria-label="Photo of hands reviewing growth charts on paper" style="background:linear-gradient(135deg,#e9edf2,#a9bccb)">
        <div class="skill-label label-left bg-green">Product Launching</div>
      </div>

      <div class="skill-photo" role="img" aria-label="Photo of guests at an evening event" style="background:linear-gradient(135deg,#4d3a3f,#b8937c)">
        <div class="skill-label label-right bg-purple">Event Co-ordination</div>
      </div>
      <div class="skill-text right">
        <h3 class="c-purple">THERE'S NOTHING QUITE LIKE A DEADLINE TO GET YOU FOCUSED</h3>
        <p>And events are like a deadline that go off with a BANG! I love the build up and milestones that events management brings to my life.</p>
      </div>
    </div>
  </section>

  <section class="experience">
    <h2 class="section-title">PROFESSIONAL EXPERIENCES</h2>
    <ul class="exp-list">
      <li><span class="exp-year">2017</span><span class="exp-desc">Started VitaLink AU – Exclusive Distributors for NutriGen (Queensland, New South Wales and Victoria)</span><span class="exp-plus">+</span></li>
      <li><span class="exp-year">2016</span><span class="exp-desc">Presented 'AK Certification Seminar – Sessions 1-4', Brisbane</span><span class="exp-plus">+</span></li>
      <li><span class="exp-year">2015</span><span class="exp-desc">Presented 'Retained Neonatal Reflexes' two-part seminar in Brisbane (February/March and August/September)</span><span class="exp-plus">+</span></li>
      <li><span class="exp-year">2014</span><span class="exp-desc">Presented 'Retained Neonatal Reflexes – An Overview' at ICNM International Conference</span><span class="exp-plus">+</span></li>
      <li><span class="exp-year">2014</span><span class="exp-desc">Presented 'Retained Neonatal Reflexes' two-part seminar in Sydney</span><span class="exp-plus">+</span></li>
      <li><span class="exp-year">2013</span><span class="exp-desc">Invited by ICNM Austria to present 'Retained Neonatal Reflexes' seminar in Austria (September 9-13)</span><span class="exp-plus">+</span></li>
      <li><span class="exp-year">2012</span><span class="exp-desc">CoreMotion Clinic won Australian Excellence Award for Service Excellence with 97.7% satisfaction rating</span><span class="exp-plus">+</span></li>
      <li><span class="exp-year">2011</span><span class="exp-desc">CoreMotion Clinic won Northside Business Achievers Award 2010 for Healthcare category for Brisbane City North</span><span class="exp-plus">+</span></li>
    </ul>
  </section>

  <section class="education">
    <h2 class="section-title">EDUCATION</h2>
    <p class="edu-intro">Life is for learning. And the more I learn, the more curious I become. I have a thirst to understand things and am passionately inquisitive. My patients and my children are my greatest teachers. But here are my formal foundation studies.</p>
    <div class="timeline-line"></div>
    <div class="edu-step" style="top:216px">01</div>
    <div class="edu-item right" style="top:222px"><h4>INTERNATIONAL COLLEGE OF NEURO-MUSCULAR STUDIES</h4>DIPLOMATE OF THE INTERNATIONAL BOARD OF NEURO-MUSCULAR STUDIES<br>BOARD OF CERTIFIED TEACHERS, BRISBANE 2008</div>
    <div class="edu-step" style="top:316px">02</div>
    <div class="edu-item left" style="top:320px"><h4>HARBOURSIDE UNIVERSITY</h4>MASTER OF CHIROPRACTIC, SYDNEY, AUSTRALIA 2000-2002</div>
    <div class="edu-step" style="top:414px">03</div>
    <div class="edu-item right" style="top:418px"><h4>EASTBANK UNIVERSITY</h4>BACHELOR OF SCIENCE (ANATOMY), BRISBANE, AUSTRALIA 1997-1999</div>
    <div class="edu-step" style="top:476px">04</div>
    <div class="edu-item left" style="top:470px"><h4>RIVERGLEN STATE HIGH SCHOOL</h4>1991-1996</div>
    <p class="edu-quote">"Education is not preparation for life; Education is life itself."</p>
  </section>

  <section class="employment">
    <h2 class="section-title">EMPLOYMENT</h2>
    <div class="jobs">
      <div class="job">
        <h4>COREMOTION CLINIC</h4>
        <div class="role">PRINCIPAL CHIROPRACTOR</div>
        <div class="years">2005-2017</div>
        <p>What a wonderful place to work! I can't come to this clinic and not feel happy. It's decorated for the hundreds of children who get treated here. I've been privileged to watch so many families blossom through the stages of infancy to teens. They feel like family.</p>
      </div>
      <div class="job">
        <h4>NORTHSHORE SPINE &amp; WELLNESS</h4>
        <div class="role">ASSOCIATE CHIROPRACTOR</div>
        <div class="years">2004-2005</div>
        <p>I learned a lot from my mentor here. He taught me how to think like a business owner, which was exactly what I needed for my next move.</p>
      </div>
      <div class="job">
        <h4>BRIGHTPATH FAMILY CENTRE</h4>
        <div class="role">ASSOCIATE CHIROPRACTOR</div>
        <div class="years">2003-2004</div>
        <p>Working under the clinic founder has been the greatest gift I could have imagined fresh out of University. He taught me his life's learnings and I have treasured them. He taught me that the greatest gift for any teacher is to have their student surpass them.</p>
      </div>
      <div class="job">
        <h4>HARBOURSIDE UNIVERSITY</h4>
        <div class="role">CLINICAL SKILLS TUTOR AND LECTURER</div>
        <div class="years">2002-2003</div>
        <p>What an honour to be invited to tutor and examine 2nd year Chiropractic Skills whilst in my final year of my Masters of Chiropractic. And what a delightful bunch of students we had that year too!</p>
      </div>
    </div>
  </section>

  <section class="sites">
    <h2 class="section-title">MY SITES</h2>
    <div class="site-grid">
      <div class="site-card light">dr Megan blog</div>
      <div class="site-card dark">VitaLink AU</div>
      <div class="site-card light"><span class="site-dot"></span>learnNM.com.au</div>
      <div class="site-card light">Reflex Path</div>
    </div>
  </section>

  <section class="contact">
    <div class="contact-photo" role="img" aria-label="Dimmed photo of a clinic shelf and desk in warm tones"></div>
    <h2 class="contact-title">CONTACT</h2>
    <div class="contact-sub">ASHWOOD PARK Brisbane</div>
    <div class="field" style="top:128px">Your Name</div>
    <div class="field" style="top:171px">Your Email</div>
    <div class="field" style="top:212px">Your Phone Number</div>
    <div class="field" style="top:255px">Your Message</div>
    <div class="submit">Submit</div>
  </section>

  <section class="footer">
    <div class="copyright">© 2017 DR MEGAN HOLT</div>
    <div class="footer-brand">dr Megan Holt</div>
    <span class="social" style="left:640px"></span>
    <span class="social" style="left:676px"></span>
  </section>

</main>
</body>
</html>
```